Employees at R&T Gale Power Services need new modern business cards

We need new business cards that showcase our new rebranded logo. We are seeking modern, clean, fresh, attractive cards while still being professional. We want to stand out. A little bit about us: we work in Canada and the USA. We offer Technical Field Advisors to support wind turbine manufacturers through the construction phase of wind farms. I am attaching a mock inspiration picture to lead you in the direction we want to see this go. Also, FYI We have approx. 10/11 different employees that would need their own card. Let me know when you would need everyone's name. We would love to see some black and white options as well as color copies- when using colors we want green to be the dominant color with accents for blue and orange (colors should match our logo). I have also attached copies of our old business card for reference.

Contact Information for Business Card

Name, Telephone, Email, address, company name, website. EXAMPLE: Dean Whitlock, DeanWhitlock@randtgale.net, 555-384-9162, 318276 Fallow Line #7, Marrowby, ON X9Z 4Q2, www.randtgale.net

Colors
0054AA
0677BA
7BADD7
CADEEF
E8F1F8
00AB8E
00BBA5
67D7C9
C6EFE9
E9F9F6
F0912C
F2A743
F7CA91
FBE8D2
FDF5EE

Requirements
Must have
• 2 sided business card

```html
<!DOCTYPE html>
<html lang="en">
<head>
<meta charset="utf-8">
<title>R&amp;T Gale Power Services – Business Card</title>
<link href="https://fonts.googleapis.com/css2?family=Montserrat:wght@400;700&display=swap" rel="stylesheet">
<style>
  :root {
    --page: #c9c9c9;
    --card-light: #ffffff;
    --card-dark: #282828;
    --green: #3bb54a;
    --blue: #0a72bb;
    --blue-light: #2196d4;
    --orange: #f7931e;
    --text: #3a3a3a;
  }
  * { margin: 0; padding: 0; box-sizing: border-box; }
  html, body { width: 1125px; height: 1200px; overflow: hidden; }
  body {
    background: var(--page);
    font-family: "Montserrat", Arial, sans-serif;
    color: var(--text);
    position: relative;
  }
  .card {
    position: absolute;
    left: 178px;
    width: 770px;
    height: 438px;
    border-radius: 22px;
    overflow: hidden;
    box-shadow: 1px 2px 3px rgba(0,0,0,0.45);
  }
  .card--front { top: 140px; background: var(--card-light); }
  .card--back { top: 626px; background: var(--card-dark); }

  .brand {
    position: absolute;
    display: flex;
    flex-direction: column;
    align-items: center;
    text-align: center;
  }
  .brand__dot {
    border-radius: 50%;
    background: var(--green);
  }
  .brand__name {
    font-weight: 700;
    color: var(--green);
    line-height: 1.1;
    letter-spacing: 0.04em;
    text-transform: uppercase;
  }
  .card--front .brand { left: 60px; top: 111px; width: 300px; }
  .card--front .brand__dot { width: 124px; height: 124px; margin-bottom: 20px; }
  .card--front .brand__name { font-size: 22px; }

  .card--back .brand { left: 0; right: 0; top: 99px; }
  .card--back .brand__dot { width: 155px; height: 155px; margin-bottom: 24px; }
  .card--back .brand__name { font-size: 30px; }

  .divider {
    position: absolute;
    left: 384px;
    top: 103px;
    width: 1.5px;
    height: 205px;
    background: var(--orange);
  }
  .contact {
    position: absolute;
    left: 420px;
    top: 96px;
  }
  .contact__name {
    font-size: 32px;
    font-weight: 700;
    color: var(--green);
    letter-spacing: 0.01em;
    line-height: 1.1;
  }
  .contact__role { font-size: 19px; margin-top: 2px; }
  .contact__list { list-style: none; margin-top: 14px; }
  .contact__item {
    display: flex;
    align-items: center;
    gap: 6px;
    font-size: 18.5px;
    height: 30px;
  }
  .contact__icon { width: 14px; height: 14px; flex: none; }
  .contact__address { font-size: 19.5px; line-height: 1.3; margin-top: 18px; }

  .accent-band {
    position: absolute;
    left: 0;
    right: 0;
    bottom: 0;
    height: 80px;
    background: linear-gradient(90deg, var(--blue) 0%, var(--blue) 70%, var(--blue-light) 100%);
  }
</style>
</head>
<body>

<section class="card card--front" aria-label="Business card front">
  <div class="brand">
    <span class="brand__dot"></span>
    <span class="brand__name">R&amp;T Gale<br>Power Services</span>
  </div>

  <div class="divider"></div>

  <div class="contact">
    <h1 class="contact__name">DEAN WHITLOCK</h1>
    <p class="contact__role">CEO/Founder</p>
    <ul class="contact__list">
      <li class="contact__item">
        <svg class="contact__icon" viewBox="0 0 16 16" aria-hidden="true"><path fill="var(--blue)" d="M3 1.5l2.5 2.8-1.4 1.6c.9 2 2.3 3.4 4.3 4.3l1.6-1.4 2.8 2.5-1.6 2.2C6.5 13.2 2.8 9.5 1 3.1z"/></svg>
        555-384-9162
      </li>
      <li class="contact__item">
        <svg class="contact__icon" viewBox="0 0 16 16" aria-hidden="true"><rect x="1" y="3" width="14" height="10" rx="1" fill="var(--blue)"/><path d="M1.5 4l6.5 5 6.5-5" stroke="#fff" stroke-width="1.4" fill="none"/></svg>
        DeanWhitlock@randtgale.net
      </li>
      <li class="contact__item">
        <svg class="contact__icon" viewBox="0 0 16 16" aria-hidden="true"><g fill="none" stroke="var(--blue)" stroke-width="1.2"><circle cx="8" cy="8" r="6.5"/><ellipse cx="8" cy="8" rx="3" ry="6.5"/><path d="M1.5 8h13M2.5 4.8h11M2.5 11.2h11"/></g></svg>
        www.randtgale.net
      </li>
    </ul>
    <p class="contact__address">318276 Fallow Line #7<br>Marrowby, ON X9Z 4Q2</p>
  </div>

  <div class="accent-band" role="img" aria-label="Decorative wave band in blue with green and orange accents"></div>
</section>

<section class="card card--back" aria-label="Business card back">
  <div class="brand">
    <span class="brand__dot"></span>
    <span class="brand__name">R&amp;T Gale<br>Power Services</span>
  </div>
</section>

</body>
</html>
```